3 pages for Quillmoney.com (design required, not ecommerce coding)

We are a new start up specialising exclusively in enabling e-commerce in Africa so that African businesses can place a "buy now" button on products and services they offer on the internet. The mechanism that powers this is heavily grounded in mobile payments.

Because of this, the service will also be used for in-shop and person-to-person payments.

The main objective for looking for a professional design is to encourage people and business owners that land on the website from computers or web devices to be impressed by its appeal and message and then eventually sign up.

We would like to see good use of black fonts on yellow backgrounds in the design.

Website source code attached.

Target Market(s)

Africa - Countries like Ghana, Nigeria, Cameroon, Zimbabwe, South Africa, etc.

Industry/Entity Type

E-Commerce

Number of Pages Required

3 page

Font styles to use
Sans Serif

Requirements
Must have
• Key requirements of this design:
• 1. Suggest a simple text based logo
• 2. The design should be mobile responsive - current template is responsive
• 3. Pages:
• 1. Main Page: Should have a large graphic explaining our purpose. I have attached one we commissioned earlier. The final one should be bigger, maybe 940x400. Current illustrations shifted to the right and a large "Sign Up" button on the left. Under the graphic, should be a keyword heavy message to the visitor
• 2. Business and Shops page (business.php):
• Should have a large graphic maybe 940x400 illustrating the quillmoney to businesses. Narrative should be on the right. It should show a "Pay with Quillmoney" button and a click hovering and text to the right. This shows the narrative for online use. There should also be an illustration for in shop payments.
• The left of the graphic should be a larger "Sign Up" button for registering.
• 3. register page: registration requirements:
• 1. Mobile phone - text
• 2. Email address - text
• 3. City - drop down
• 4. Country - drop down
• 5. Password
• 6. Confirm Password
• Website source code attached.
Nice to have
• lots of yellow background... under black text ..
Should not have
• We are not big on flash.
• Also, this is not for ecommerce coding. we are more interested in the design.

```html
<!DOCTYPE html>
<html lang="en">
<head>
<meta charset="utf-8">
<title>Quillmoney — Mobile payments for African business</title>
<link href="https://fonts.googleapis.com/css2?family=Lato:wght@400;700;900&family=Noto+Serif:wght@400;700&display=swap" rel="stylesheet">
<style>
:root{
  --yellow:#f6b400;
  --yellow-deep:#e9a800;
  --yellow-soft:#f9c93a;
  --ink:#1d1d1d;
  --text:#6f6f6f;
  --muted:#9a9a9a;
  --line:#e6e6e6;
  --white:#ffffff;
  --footer:#222222;
  --footer-deep:#161616;
  --footer-text:#8d8d8d;
}
*{box-sizing:border-box;margin:0;padding:0}
html,body{width:1200px;height:2908px;overflow:hidden;background:var(--white)}
body{font-family:"Lato",Arial,sans-serif;color:var(--text);font-size:13px;line-height:1.6}
.wrap{width:1000px;margin:0 auto;position:relative;height:100%}
section,header,footer{position:relative;width:1200px}

/* header */
.site-header{height:92px;border-bottom:1px solid var(--line)}
.brand{position:absolute;left:0;top:26px;font-weight:900;font-size:30px;letter-spacing:1px;color:var(--ink);text-transform:uppercase;display:flex;align-items:center;gap:10px}
.brand-mark{width:18px;height:18px;background:var(--yellow)}
.main-nav{position:absolute;right:0;top:36px;display:flex;gap:34px;font-size:11px;letter-spacing:1.5px;text-transform:uppercase;color:var(--muted)}
.main-nav .current{color:var(--ink);font-weight:700}

/* buttons */
.btn{display:inline-block;border:2px solid var(--ink);color:var(--ink);font-size:11px;font-weight:700;letter-spacing:1.5px;text-transform:uppercase;padding:10px 18px;background:transparent}

/* hero */
.hero{height:386px;background:var(--yellow)}
.hero-art{position:absolute;left:140px;top:20px;width:940px;height:260px;background:linear-gradient(135deg,var(--yellow-soft),var(--yellow-deep));border-radius:4px}
.hero .btn{position:absolute;left:0;top:300px}

/* features */
.features{height:312px;border-bottom:1px solid var(--line)}
.feature-row{position:absolute;left:0;top:70px;width:1000px;display:flex}
.feature{width:250px;text-align:center;padding:0 30px}
.ring{width:48px;height:48px;border:2px solid var(--yellow);border-radius:50%;margin:0 auto 22px;display:flex;align-items:center;justify-content:center}
.feature h3{font-family:"Noto Serif",Georgia,serif;font-weight:400;font-size:17px;color:var(--ink);margin-bottom:10px}
.feature p{font-size:11.5px;line-height:1.7;color:var(--muted)}

/* yellow grid */
.benefits{height:578px;background:var(--yellow)}
.benefit-grid{position:absolute;left:0;top:128px;width:1000px;display:grid;grid-template-columns:repeat(3,330px);row-gap:70px}
.benefit{padding-right:40px}
.benefit h4{display:flex;align-items:center;gap:14px;font-family:"Noto Serif",Georgia,serif;font-weight:400;font-size:16px;color:var(--ink);margin-bottom:10px}
.benefit p{padding-left:34px;font-size:11.5px;line-height:1.75;color:#fff6dc}

/* phone section */
.showcase{height:644px}
.point{position:absolute;left:0;width:600px;display:flex;align-items:flex-start}
.point-text{width:410px;text-align:right;padding-right:30px;margin-right:70px}
.point-text h4{font-family:"Noto Serif",Georgia,serif;font-weight:400;font-size:16px;color:var(--ink);margin-bottom:10px}
.point-text p{font-size:11.5px;line-height:1.7;color:var(--muted)}
.point .ring{margin:0;width:56px;height:56px;border-width:3px}
.device{position:absolute;left:640px;top:14px;width:170px;height:580px;border-radius:26px;background:linear-gradient(180deg,#f3f3f3,#dcdcdc)}
.device-screen{position:absolute;left:14px;top:92px;width:142px;height:398px;background:var(--yellow)}

/* quote band */
.callout{height:274px;background:var(--yellow);text-align:center}
.callout blockquote{position:absolute;left:150px;top:58px;width:700px;font-family:"Noto Serif",Georgia,serif;font-size:20px;line-height:1.6;color:var(--ink)}
.callout .btn{position:absolute;left:450px;top:172px}

/* footer */
.site-footer{height:526px;background:var(--footer);color:var(--footer-text)}
.to-top{position:absolute;left:480px;top:34px;width:40px;height:40px;display:flex;align-items:center;justify-content:center}
.footer-rule{position:absolute;left:0;top:110px;width:1000px;height:1px;background:#333}
.col{position:absolute;top:180px}
.col h5{font-size:11px;letter-spacing:1.5px;text-transform:uppercase;color:#cfcfcf;font-weight:700;margin-bottom:16px}
.col p{font-size:11.5px;line-height:1.7}
.col-about{left:0;width:250px}
.col-posts{left:310px;width:310px}
.col-gallery{left:680px;width:260px}
.social{display:flex;gap:6px;margin-top:12px}
.social span{width:26px;height:26px;border:2px solid var(--yellow)}
.post{margin-bottom:14px}
.post a{color:var(--yellow)}
.post time{display:block;font-size:10px;color:#5f5f5f}
.gallery{display:grid;grid-template-columns:repeat(3,78px);gap:6px}
.gallery div{height:70px;background:linear-gradient(135deg,#6e6a66,#a39d94)}
.legal{height:96px;background:var(--footer-deep);color:#6b6b6b;font-size:10.5px}
.legal p{position:absolute;left:0;top:40px}
</style>
</head>
<body>

<header class="site-header">
  <div class="wrap">
    <div class="brand"><span class="brand-mark"></span>Quillmoney</div>
    <nav class="main-nav">
      <span class="current">Home</span>
      <span>Business &amp; Shops</span>
      <span>Register</span>
    </nav>
  </div>
</header>

<section class="hero">
  <div class="wrap">
    <div class="hero-art" role="img" aria-label="Illustration of the four steps: add money to your account, pay online or in shops, service and goods delivery guaranteed, enjoy"></div>
    <span class="btn">Sign Up</span>
  </div>
</section>

<section class="features">
  <div class="wrap">
    <div class="feature-row">
      <div class="feature">
        <div class="ring"><svg width="16" height="20" viewBox="0 0 16 20"><rect x="2" y="1" width="12" height="18" rx="2" fill="none" stroke="#1d1d1d" stroke-width="2"/><circle cx="8" cy="15" r="1.2" fill="#1d1d1d"/></svg></div>
        <h3>Add Money</h3>
        <p>Top up your wallet from any phone in seconds and keep funds ready for every purchase you make.</p>
      </div>
      <div class="feature">
        <div class="ring"><svg width="20" height="16" viewBox="0 0 20 16"><rect x="1" y="2" width="18" height="12" rx="2" fill="none" stroke="#1d1d1d" stroke-width="2"/><line x1="1" y1="6" x2="19" y2="6" stroke="#1d1d1d" stroke-width="2"/></svg></div>
        <h3>Buy Online</h3>
        <p>Press the buy now button on any partner store and confirm the payment right from your mobile.</p>
      </div>
      <div class="feature">
        <div class="ring"><svg width="20" height="16" viewBox="0 0 20 16"><rect x="1" y="3" width="11" height="9" fill="#1d1d1d"/><path d="M12 6h4l3 3v3h-7z" fill="#1d1d1d"/><circle cx="5" cy="13" r="2" fill="#1d1d1d"/><circle cx="15" cy="13" r="2" fill="#1d1d1d"/></svg></div>
        <h3>Guaranteed Delivery</h3>
        <p>Your money is held safely until the goods arrive, so every seller delivers what was promised.</p>
      </div>
      <div class="feature">
        <div class="ring"><svg width="18" height="18" viewBox="0 0 18 18"><path d="M9 1a8 8 0 1 0 0.01 0" fill="none" stroke="#1d1d1d" stroke-width="2"/><path d="M5 9l3 3 5-6" fill="none" stroke="#1d1d1d" stroke-width="2"/></svg></div>
        <h3>After Sale Services</h3>
        <p>Our friendly team helps with refunds, returns and questions long after the sale is complete.</p>
      </div>
    </div>
  </div>
</section>

<section class="benefits" role="region" aria-label="Benefits">
  <div class="wrap">
    <div class="benefit-grid">
      <div class="benefit">
        <h4><svg width="20" height="20" viewBox="0 0 20 20"><rect x="3" y="2" width="14" height="16" rx="2" fill="#1d1d1d"/></svg>Lorem Ipsum Dolor</h4>
        <p>Phasellus enim libero, blandit vel sapien vitae, condimentum ultricies magna et. Quisque euismod orci ut et lobortis aliquam. Aliquam in tortor enim.</p>
      </div>
      <div class="benefit">
        <h4><svg width="20" height="20" viewBox="0 0 20 20"><rect x="1" y="5" width="12" height="9" fill="#1d1d1d"/><path d="M13 8h4l2 3v3h-6z" fill="#1d1d1d"/><circle cx="5" cy="16" r="2" fill="#1d1d1d"/><circle cx="16" cy="16" r="2" fill="#1d1d1d"/></svg>Duis Autem Vileum</h4>
        <p>Phasellus enim libero, blandit vel sapien vitae, condimentum ultricies magna et. Quisque euismod orci ut et lobortis aliquam. Aliquam in tortor enim.</p>
      </div>
      <div class="benefit">
        <h4><svg width="20" height="20" viewBox="0 0 20 20"><circle cx="10" cy="10" r="8" fill="#1d1d1d"/></svg>Claritas Estiitaes</h4>
        <p>Phasellus enim libero, blandit vel sapien vitae, condimentum ultricies magna et. Quisque euismod orci ut et lobortis aliquam. Aliquam in tortor enim.</p>
      </div>
      <div class="benefit">
        <h4><svg width="20" height="20" viewBox="0 0 20 20"><circle cx="7" cy="7" r="3" fill="#1d1d1d"/><circle cx="14" cy="8" r="2.5" fill="#1d1d1d"/><path d="M1 17a6 6 0 0 1 12 0zM11 17a4 4 0 0 1 8 0z" fill="#1d1d1d"/></svg>Typi Non Habent</h4>
        <p>Phasellus enim libero, blandit vel sapien vitae, condimentum ultricies magna et. Quisque euismod orci ut et lobortis aliquam. Aliquam in tortor enim.</p>
      </div>
      <div class="benefit">
        <h4><svg width="20" height="20" viewBox="0 0 20 20"><rect x="2" y="4" width="16" height="12" fill="#1d1d1d"/></svg>Mirum Est Notare</h4>
        <p>Phasellus enim libero, blandit vel sapien vitae, condimentum ultricies magna et. Quisque euismod orci ut et lobortis aliquam. Aliquam in tortor enim.</p>
      </div>
      <div class="benefit">
        <h4><svg width="20" height="20" viewBox="0 0 20 20"><path d="M2 3h16v11H8l-4 4v-4H2z" fill="#1d1d1d"/></svg>Eodem Modo Typi</h4>
        <p>Phasellus enim libero, blandit vel sapien vitae, condimentum ultricies magna et. Quisque euismod orci ut et lobortis aliquam. Aliquam in tortor enim.</p>
      </div>
    </div>
  </div>
</section>

<section class="showcase">
  <div class="wrap">
    <div class="point" style="top:80px">
      <div class="point-text"><h4>Lorem Ipsum Dolor</h4><p>Lorem ipsum dolor sit amet, consectetuer adipiscing elit, sed diam nonummy nibh euismod tincidunt ut laoreet dolore magna aliquam erat volutpat.</p></div>
      <div class="ring"><svg width="18" height="18" viewBox="0 0 20 20"><path d="M10 1l2.6 6 6.4.5-4.9 4.2 1.5 6.3L10 14.7 4.4 18l1.5-6.3L1 7.5 7.4 7z" fill="#1d1d1d"/></svg></div>
    </div>
    <div class="point" style="top:236px">
      <div class="point-text"><h4>Duis Autem Vileum</h4><p>Ut wisi enim ad minim veniam, quis nostrud exerci tation ullamcorper suscipit lobortis nisl ut aliquip ex ea commodo consequat duis autem vel eum.</p></div>
      <div class="ring"><svg width="18" height="18" viewBox="0 0 20 20"><path d="M10 1l2.6 6 6.4.5-4.9 4.2 1.5 6.3L10 14.7 4.4 18l1.5-6.3L1 7.5 7.4 7z" fill="#1d1d1d"/></svg></div>
    </div>
    <div class="point" style="top:394px">
      <div class="point-text"><h4>Typi Non Habent</h4><p>Nam liber tempor cum soluta nobis eleifend option congue nihil imperdiet doming id quod mazim placerat facer possim assum typi non habent.</p></div>
      <div class="ring"><svg width="18" height="18" viewBox="0 0 20 20"><path d="M10 1l2.6 6 6.4.5-4.9 4.2 1.5 6.3L10 14.7 4.4 18l1.5-6.3L1 7.5 7.4 7z" fill="#1d1d1d"/></svg></div>
    </div>
    <div class="device" role="img" aria-label="Photo of a white smartphone showing the Quillmoney app on a yellow screen"><div class="device-screen"></div></div>
  </div>
</section>

<section class="callout">
  <div class="wrap">
    <blockquote>Mirum est notare quam littera gothica, quam nunc putamus parum claram, anteposuerit litterarum formas humanitatis per seacula quarta decima.</blockquote>
    <span class="btn">Sign Up</span>
  </div>
</section>

<footer class="site-footer">
  <div class="wrap">
    <div class="to-top"><svg width="20" height="12" viewBox="0 0 20 12"><path d="M2 10l8-8 8 8" fill="none" stroke="#ffffff" stroke-width="3"/></svg></div>
    <div class="footer-rule"></div>
    <div class="col col-about">
      <h5>About Quillmoney</h5>
      <p>Lorem ipsum dolor sit amet, consectetuer adipiscing elit, sed diam nonummy nibh euismod tincidunt ut laoreet dolore magna aliquam erat volutpat. Ut wisi enim ad minim veniam, quis nostrud.</p>
      <h5 style="margin-top:26px">Connect With Us</h5>
      <div class="social"><span></span><span></span><span></span><span></span><span></span><span></span></div>
    </div>
    <div class="col col-posts">
      <h5>Chirpline</h5>
      <div class="post"><p>Mobile payments are growing fast across the region, see how <a>quillmoney.com</a> keeps sellers paid.</p><time>12:45 PM Jun 9th</time></div>
      <div class="post"><p>New shops joined this week, welcome to all of them <a>quillmoney.com/shops</a></p><time>10:12 AM Jun 7th</time></div>
      <div class="post"><p>Thank you <a>@quillmoney</a> for the quick refund, great service as always from the team.</p><time>08:30 AM Jun 5th</time></div>
    </div>
    <div class="col col-gallery">
      <h5>Snapwall</h5>
      <div class="gallery" role="img" aria-label="Grid of nine portrait photos of customers">
        <div></div><div></div><div></div><div></div><div></div><div></div><div></div><div></div><div></div>
      </div>
    </div>
  </div>
</footer>

<section class="legal">
  <div class="wrap"><p>© Copyright 2013 Quillmoney</p></div>
</section>

</body>
</html>
```